Specialised investor in e-mobility and energy wants business card design

We need a business card design that fits our existing corporate design. <The look and feel must be 'sharp'/'clean', dynamic, communicate momentum, professionalism etc (as one would imagine from a firm in the financial sector). We like the idea of a reverse-side of the card that includes the logo, and the name and contact details on the other. We expect the deliverable to be whatever format might be required to be able to get cards printed directly by a service such as tandor press. Our website is www.orm.capital

```html
<!DOCTYPE html>
<html lang="en">
<head>
<meta charset="utf-8">
<title>ORM Capital – Business Card</title>
<link rel="stylesheet" href="https://fonts.googleapis.com/css2?family=Poppins:wght@400;600&display=swap">
<style>
  :root {
    --backdrop: #2c2c2c;
    --card-white: #ffffff;
    --brand-green: #2f4f22;
    --deep-green: #324f23;
    --accent-green: #6fd24c;
    --ink: #1c1c1c;
    --divider: #b8b8b8;
  }
  * { margin: 0; padding: 0; box-sizing: border-box; }
  html, body {
    width: 1093px;
    height: 1200px;
    overflow: hidden;
    background: var(--backdrop);
    font-family: "Poppins", sans-serif;
  }
  .card {
    position: absolute;
    left: 265px;
    width: 578px;
    height: 356px;
    border-radius: 24px;
  }
  .card--front { top: 226px; background: var(--card-white); }
  .card--back { top: 621px; background: var(--deep-green); }

  .brand-name {
    position: absolute;
    font-weight: 400;
    white-space: nowrap;
    letter-spacing: 0.5px;
  }
  .card--front .brand-name {
    left: 28px;
    top: 158px;
    font-size: 38px;
    color: var(--brand-green);
  }
  .card--back .brand-name {
    left: 0;
    right: 0;
    top: 130px;
    text-align: center;
    font-size: 62px;
    color: var(--accent-green);
  }

  .divider {
    position: absolute;
    left: 289px;
    top: 74px;
    width: 1px;
    height: 208px;
    background: linear-gradient(to bottom, transparent, var(--divider) 20%, var(--divider) 80%, transparent);
  }

  .details {
    position: absolute;
    left: 311px;
    top: 88px;
    color: var(--ink);
  }
  .person-name {
    font-size: 22px;
    font-weight: 600;
    line-height: 26px;
    color: var(--brand-green);
    letter-spacing: 0.3px;
  }
  .person-role {
    font-size: 16.5px;
    line-height: 18px;
    color: #333;
  }
  .contact-list {
    list-style: none;
    margin-top: 14px;
  }
  .contact-list li {
    display: flex;
    align-items: center;
    font-size: 17px;
    line-height: 21px;
  }
  .contact-list svg {
    width: 15px;
    height: 15px;
    margin-right: 7px;
    fill: var(--brand-green);
    flex: none;
  }
  .web-highlight { color: var(--brand-green); }
  .address {
    margin-top: 13px;
    font-size: 17px;
    line-height: 21px;
  }
</style>
</head>
<body>
  <section class="card card--front">
    <div class="brand-name">ORM Capital</div>
    <div class="divider"></div>
    <div class="details">
      <h1 class="person-name">JONATHAN SMITH</h1>
      <p class="person-role">Managing Director</p>
      <ul class="contact-list">
        <li>
          <svg viewBox="0 0 24 24" aria-hidden="true"><path d="M6.6 10.8c1.4 2.8 3.8 5.1 6.6 6.6l2.2-2.2c.3-.3.7-.4 1-.2 1.1.4 2.3.6 3.6.6.6 0 1 .4 1 1V20c0 .6-.4 1-1 1C10.6 21 3 13.4 3 4c0-.6.4-1 1-1h3.5c.6 0 1 .4 1 1 0 1.3.2 2.5.6 3.6.1.3 0 .7-.2 1l-2.3 2.2z"/></svg>
          044-123 456 789
        </li>
        <li>
          <svg viewBox="0 0 24 24" aria-hidden="true"><path d="M2 5h20v14H2z M3.5 6.5 12 13l8.5-6.5" fill="var(--brand-green)"/><path d="M3 6l9 7 9-7" stroke="#fff" stroke-width="1.5" fill="none"/></svg>
          info@webname.com
        </li>
        <li>
          <svg viewBox="0 0 24 24" aria-hidden="true"><circle cx="12" cy="12" r="9.5" fill="none" stroke="var(--brand-green)" stroke-width="2"/><path d="M2.5 12h19M12 2.5v19M12 2.5c-5 5-5 14 0 19M12 2.5c5 5 5 14 0 19M4.5 7h15M4.5 17h15" fill="none" stroke="var(--brand-green)" stroke-width="1.5"/></svg>
          www.<span class="web-highlight">websitename</span>.com
        </li>
      </ul>
      <p class="address">421, Address line goes here<br>45452,Country Name</p>
    </div>
  </section>

  <section class="card card--back">
    <div class="brand-name">ORM Capital</div>
  </section>
</body>
</html>
```